The Brightwater Compass Business Card

We need an attractive business card with the logo that we bought from ArtVantly last year.
Our mission is to contribute to change the way today's leaders manage business companies bringing value to the workplace and helping them to build a new model of creating wealth.
Our logo is clear about our values : we seek Positive Change through People and are convinced that the pursuit of individual well-being and the chase of economic results can converge with the right management.
Management Consulting
Corinne Fabrelle
+34 612 98 70 31
corinne.fabrelle@thebrightwatercompass-mail.net
www.thebrightwatercompass-mail.net

```html
<!DOCTYPE html>
<html lang="en">
<head>
<meta charset="utf-8">
<title>The Brightwater Compass – Business Card</title>
<link rel="stylesheet" href="https://fonts.googleapis.com/css2?family=Noto+Serif:wght@400;700&display=swap">
<style>
  :root {
    --backdrop: #b3b4b7;
    --card-white: #f5f6f8;
    --mint: #cfe6e2;
    --mint-light: #d6ebe7;
    --mint-shade: #bcd7d2;
    --teal: #13a994;
    --ink: #0f7a74;
    --shadow: rgba(40, 70, 66, 0.35);
  }
  html, body {
    margin: 0;
    width: 1200px;
    height: 1200px;
    overflow: hidden;
    background: var(--backdrop);
  }
  .card-canvas { display: block; width: 1200px; height: 1200px; }
  .holder-name {
    font-family: "Noto Serif", Georgia, serif;
    font-size: 62px;
    font-weight: 400;
    fill: var(--ink);
    letter-spacing: 1px;
  }
  .contact-line {
    font-family: "Noto Serif", Georgia, serif;
    font-weight: 700;
    font-size: 29px;
    fill: var(--ink);
  }
  .contact-line.email { font-size: 24px; }
  .brand-name {
    font-family: "Noto Serif", Georgia, serif;
    font-weight: 400;
    font-size: 30px;
    fill: #ffffff;
  }
  .contact-icon { fill: var(--ink); }
</style>
</head>
<body>
<svg class="card-canvas" viewBox="0 0 1200 1200" xmlns="http://www.w3.org/2000/svg">
  <defs>
    <clipPath id="card-shape">
      <rect x="22" y="278" width="1141" height="652" rx="28"/>
    </clipPath>
    <linearGradient id="edge-shadow" x1="0" y1="0" x2="0" y2="1">
      <stop offset="0" stop-color="#2c4a46" stop-opacity="0"/>
      <stop offset="1" stop-color="#2c4a46" stop-opacity="0.35"/>
    </linearGradient>
    <filter id="soft-drop" x="-20%" y="-20%" width="140%" height="140%">
      <feDropShadow dx="4" dy="8" stdDeviation="8" flood-color="#1d3d39" flood-opacity="0.35"/>
    </filter>
    <filter id="text-drop">
      <feDropShadow dx="2" dy="3" stdDeviation="2" flood-color="#000" flood-opacity="0.25"/>
    </filter>
  </defs>

  <!-- card -->
  <g class="business-card" clip-path="url(#card-shape)">
    <rect class="card-base" x="22" y="278" width="1141" height="652" fill="var(--card-white)"/>

    <!-- mint upper area -->
    <polygon class="mint-field" points="22,278 1163,278 1163,578 22,880" fill="var(--mint)"/>

    <!-- layered band under the right panel -->
    <polygon class="mint-band" points="830,560 1163,470 1163,578 850,662" fill="var(--mint-shade)"/>

    <!-- right raised panel -->
    <polygon class="mint-panel" points="755,278 1163,278 1163,508 838,595" fill="var(--mint-light)" filter="url(#soft-drop)"/>

    <!-- teal brand tile -->
    <g class="brand-tile" transform="rotate(-15.5 690 500)" filter="url(#soft-drop)">
      <rect x="545" y="355" width="300" height="300" rx="48" fill="var(--teal)"/>
      <circle cx="695" cy="440" r="14" fill="#ffffff"/>
      <text class="brand-name" x="695" y="520" text-anchor="middle">The Brightwater</text>
      <text class="brand-name" x="695" y="562" text-anchor="middle">Compass</text>
    </g>

    <!-- shadow along the white diagonal edge -->
    <polygon class="edge-shade" points="350,720 1163,500 1163,578 22,880" fill="url(#edge-shadow)" opacity="0.55"/>
    <polygon class="white-field" points="22,880 1163,578 1163,930 22,930" fill="var(--card-white)"/>
  </g>

  <!-- holder name -->
  <g class="holder" transform="rotate(-15.5 75 575)">
    <text class="holder-name" x="75" y="575">CORINNE</text>
    <text class="holder-name" x="185" y="650">FABRELLE</text>
  </g>

  <!-- contact details -->
  <g class="contacts" transform="rotate(-15.5 275 860)" filter="url(#text-drop)">
    <g class="contact-icon" transform="translate(232 840)">
      <rect x="0" y="0" width="28" height="19" rx="2"/>
      <polyline points="1,1 14,11 27,1" fill="none" stroke="var(--card-white)" stroke-width="2"/>
    </g>
    <text class="contact-line email" x="275" y="858">corinne.fabrelle@thebrightwatercompass-mail.net</text>

    <path class="contact-icon" d="M0 0 L0 22 L6 16 L10 25 L13 24 L9 15 L17 15 Z" transform="translate(382 877)"/>
    <text class="contact-line" x="420" y="902">www.thebrightwatercompass-mail.net</text>

    <path class="contact-icon" d="M3 1 C1 2 0 5 1 8 C3 14 8 19 14 21 C17 22 20 21 21 19 L21 16 L16 13 L13 15 C10 14 8 12 7 9 L9 6 L6 1 Z" transform="translate(570 927)"/>
    <text class="contact-line" x="602" y="946">+34 612 98 70 31</text>
  </g>
</svg>
</body>
</html>
```